hi all

Im after a new age looking business card with my company logo on it

must include these details, I would like the PH and Email to be symbols

If the colours used for card could be kept within the colours used in logo that I have supplied that would be great, if another colour is to be used dark grey would be ok. no light bulbs etc thanks

Details below to be incorporated on card

Damian Holloway

Lic E871302

PH 0219647381

E info@brightvaleelectrical.example.nz

Domestic Commercial Industrial Electricians

```html
<!DOCTYPE html>
<html lang="en">
<head>
<meta charset="utf-8">
<title>Brightvale Electrical — Business Card</title>
<link href="https://fonts.googleapis.com/css2?family=Montserrat:wght@400;500;700;800&display=swap" rel="stylesheet">
<style>
  :root {
    --stage: #232428;
    --card-white: #ffffff;
    --brand-blue: #0b72bd;
    --ink: #111111;
    --muted: #6f6f6f;
    --rule: #a9a9a9;
    --grey-light: #8c8d8f;
    --grey-mid: #6a6b6d;
    --grey-dark: #4f5052;
    --band-text: #ffffff;
  }
  * { box-sizing: border-box; margin: 0; padding: 0; }
  html, body {
    width: 1200px; height: 900px; overflow: hidden;
    background: var(--stage);
    font-family: "Montserrat", sans-serif;
  }
  .canvas { position: relative; width: 1200px; height: 900px; }

  .card {
    position: absolute;
    width: 540px; height: 310px;
    border-radius: 3px;
    box-shadow: 0 18px 40px rgba(0,0,0,.45);
    overflow: hidden;
  }

  /* Front */
  .card--front { left: 90px; top: 110px; background: var(--card-white); }
  .front__brand {
    position: absolute; left: 0; top: 0; width: 270px; height: 310px;
    display: flex; flex-direction: column; align-items: center; justify-content: center;
  }
  .wordmark { display: flex; align-items: center; gap: 10px; }
  .wordmark__dot {
    width: 22px; height: 22px; border-radius: 50%;
    background: var(--brand-blue);
  }
  .wordmark__name {
    color: var(--brand-blue); font-weight: 700; font-size: 17px;
    letter-spacing: 1.5px; text-transform: uppercase; line-height: 1.15;
  }
  .front__licence {
    margin-top: 26px; color: var(--muted); font-size: 12px; letter-spacing: .5px;
  }
  .front__divider {
    position: absolute; left: 270px; top: 48px; width: 1px; height: 214px;
    background: var(--rule);
  }
  .front__details {
    position: absolute; left: 300px; top: 92px; right: 16px;
  }
  .details__name { font-weight: 800; font-size: 17px; color: var(--ink); margin-bottom: 16px; }
  .contact { display: flex; align-items: center; gap: 8px; margin-bottom: 10px;
    font-size: 11px; color: var(--ink); white-space: nowrap; }
  .contact__icon {
    flex: none; width: 18px; height: 18px; border-radius: 50%;
    background: var(--brand-blue); display: flex; align-items: center; justify-content: center;
  }
  .contact__icon svg { width: 10px; height: 10px; }

  /* Back */
  .card--back {
    left: 570px; top: 480px;
    background: radial-gradient(ellipse at 50% 40%, var(--grey-light) 0%, var(--grey-mid) 55%, var(--grey-dark) 100%);
  }
  .back__brand {
    position: absolute; left: 0; right: 0; top: 70px;
    display: flex; justify-content: center;
  }
  .back__brand .wordmark__dot { width: 34px; height: 34px; }
  .back__brand .wordmark__name { font-size: 28px; letter-spacing: 2.5px; }
  .back__band {
    position: absolute; left: 0; right: 0; top: 210px; height: 34px;
    background: var(--brand-blue);
    display: flex; align-items: center; justify-content: center;
    color: var(--band-text); font-size: 14px; font-weight: 500;
    letter-spacing: 1.2px; text-transform: uppercase;
  }
</style>
</head>
<body>
<main class="canvas">

  <section class="card card--front" aria-label="Business card front">
    <div class="front__brand">
      <div class="wordmark">
        <span class="wordmark__dot"></span>
        <span class="wordmark__name">Brightvale<br>Electrical</span>
      </div>
      <p class="front__licence">Lic E871302</p>
    </div>
    <div class="front__divider"></div>
    <div class="front__details">
      <h1 class="details__name">Damian Holloway</h1>
      <p class="contact">
        <span class="contact__icon" aria-label="Phone">
          <svg viewBox="0 0 24 24"><path fill="#fff" d="M6.6 10.8a15.1 15.1 0 0 0 6.6 6.6l2.2-2.2c.3-.3.7-.4 1-.2 1.1.4 2.3.6 3.6.6.6 0 1 .4 1 1V20c0 .6-.4 1-1 1A17 17 0 0 1 3 4c0-.6.4-1 1-1h3.5c.6 0 1 .4 1 1 0 1.3.2 2.5.6 3.6.1.3 0 .7-.2 1z"/></svg>
        </span>
        021 964 7381
      </p>
      <p class="contact">
        <span class="contact__icon" aria-label="Email">
          <svg viewBox="0 0 24 24"><rect x="3" y="6" width="18" height="12" rx="1.5" fill="none" stroke="#fff" stroke-width="2"/><path d="M3.5 7 12 13l8.5-6" fill="none" stroke="#fff" stroke-width="2"/></svg>
        </span>
        info@brightvaleelectrical.example.nz
      </p>
    </div>
  </section>

  <section class="card card--back" aria-label="Business card back">
    <div class="back__brand">
      <div class="wordmark">
        <span class="wordmark__dot"></span>
        <span class="wordmark__name">Brightvale<br>Electrical</span>
      </div>
    </div>
    <div class="back__band">Domestic Commercial Industrial Electricians</div>
  </section>

</main>
</body>
</html>
```